Tea standup pouch labels

Dear designers,
I need a minimalistic and modern label for my loose tea stand-up pouches (100, 250 and 500gm packs). The label should cover 70-80% of the pouch face (front and rear both).
The label will be 2 part label - Front and Rear side labels.
The labels should have a green background (Pantone Green C) with Golden or White or black colour text. Please either use the Golden logo or black logo to see which looks good with Pantone Green C background.
I am also attaching the content file and a few other files (plain circle badge) to be used in the label.
The plain circle badge should be small at the bottom left or right side of the front side. The logo should be dominant on the front page (some of the designs I received have small logo and big "100% single estate tea" and "Assam logo" as big characters on the front page which is not what I am looking for.

The font style should note simple Times new roman or Arial. It should look modern and should be something matching to the logo sentence 'Freshest possible' but should also not be in italics. Please refer to files Font style reference front and back for the style of font. Also use the same box space design on the rear - Content should be in White background; the rectangular box edges should be rounded and the border should be in dual colour - Golden and white or in black and white depending on the logo colour used (golden or black).

For the Rear page - headings could be in Golden colour or black colour depending on the logo colour you choose to use and the text can be in white colour i.e. Option 1 - Headings in golden colour and text in white colour; Option 2 - Heading in Black colour and text in white colour or any other combination that looks good - designer to decide.

Please let me know if you need any further information.

thanks,
Toral

```html
<!DOCTYPE html>
<html lang="en">
<head>
<meta charset="utf-8">
<title>Leafmark – Pouch Labels</title>
<link rel="stylesheet" href="https://fonts.googleapis.com/css2?family=Lato:wght@400;700;900&family=Barlow+Condensed:wght@500&family=Josefin+Sans:wght@200;300&display=swap">
<style>
  :root {
    --backdrop: #3a3a3c;
    --sheet: #ffffff;
    --green-deep: #0e4a37;
    --green-mid: #1a6449;
    --green-light: #23704f;
    --gold: #c9973c;
    --white: #ffffff;
    --ink: #1a1a1a;
    --sticker-ink: #1f5a3e;
  }
  * { box-sizing: border-box; margin: 0; padding: 0; }
  html, body { width: 1200px; height: 969px; overflow: hidden; }
  body { background: var(--backdrop); position: relative; font-family: "Lato", sans-serif; }

  .sheet { position: absolute; top: 44px; width: 546px; height: 882px; background: var(--sheet); }
  .sheet--front { left: 44px; }
  .sheet--rear { left: 610px; }

  .label {
    position: absolute; top: 148px; left: 54px; width: 438px; height: 734px;
    border-radius: 72px 72px 0 0; overflow: hidden;
    background:
      radial-gradient(ellipse 120% 40% at 80% 10%, rgba(255,255,255,0.07), transparent 60%),
      radial-gradient(ellipse 140% 30% at 20% 92%, rgba(255,255,255,0.06), transparent 60%),
      linear-gradient(160deg, var(--green-light) 0%, var(--green-mid) 40%, var(--green-deep) 100%);
    color: var(--white);
  }

  /* Front */
  .brand {
    position: absolute; top: 250px; left: 0; width: 100%; text-align: center;
    font-family: "Josefin Sans", sans-serif; font-weight: 200; font-size: 62px;
    letter-spacing: 8px; color: var(--gold);
  }
  .brand-dot {
    position: absolute; top: 150px; left: 169px; width: 100px; height: 100px;
    border: 3px solid var(--gold); border-radius: 50%;
  }
  .tagline {
    position: absolute; top: 485px; left: 0; width: 100%; text-align: center;
    font-family: "Josefin Sans", sans-serif; font-weight: 300; font-size: 30px; color: var(--gold);
  }
  .front-foot { position: absolute; top: 598px; left: 0; width: 100%; height: 80px; }
  .front-foot .claim, .front-foot .weight {
    position: absolute; font-family: "Barlow Condensed", sans-serif; font-weight: 500;
    font-size: 17px; line-height: 18px; color: var(--gold);
  }
  .claim { left: 60px; top: 24px; text-align: right; width: 80px; }
  .weight { left: 291px; top: 21px; }
  .divider { position: absolute; top: 16px; width: 2px; height: 50px; background: var(--gold); }
  .divider--left { left: 163px; }
  .divider--right { left: 270px; }
  .origin-badge {
    position: absolute; left: 180px; top: 3px; width: 77px; height: 77px;
    border-radius: 50%; border: 2px solid var(--gold); background: rgba(201,151,60,0.18);
  }

  /* Rear */
  .rear-title {
    position: absolute; top: 44px; left: 0; width: 100%; text-align: center;
    font-size: 17.5px; line-height: 22px; font-weight: 400; letter-spacing: 0.2px;
  }
  .copy { position: absolute; font-size: 9.3px; line-height: 11.6px; }
  .copy p + p, .copy p + h3, .copy ul + h3 { margin-top: 11px; }
  .copy h3 { font-size: 9.3px; font-weight: 700; }
  .copy ul { list-style: none; }
  .copy li::before { content: "• "; }
  .copy--story { left: 21px; top: 96px; width: 187px; }
  .copy--guide { left: 21px; top: 330px; width: 187px; }
  .copy--facts { left: 225px; top: 330px; width: 195px; }
  .copy--facts .packer { margin-top: 28px; }

  .nutrition {
    position: absolute; left: 219px; top: 96px; width: 199px; height: 228px;
    background: var(--white); padding: 5px; color: var(--ink);
  }
  .nutrition-inner { border: 2px solid var(--ink); height: 100%; padding: 7px 5px 6px; }
  .nutrition h2 { font-size: 16.4px; font-weight: 900; letter-spacing: -0.3px; line-height: 20px; white-space: nowrap; }
  .nutrition-head { display: flex; justify-content: space-between; align-items: flex-end;
    font-size: 7.4px; line-height: 9px; margin-top: 8px; padding-bottom: 4px; border-bottom: 3px solid var(--ink); }
  .nutrition-head span:last-child { width: 72px; }
  .nutrition table { width: 100%; border-collapse: collapse; font-size: 8.4px; line-height: 10px; margin-top: 5px; }
  .nutrition td { padding: 2px 0 1px; border-bottom: 1px solid var(--ink); }
  .nutrition td:last-child { text-align: right; }
  .nutrition .indent { padding-left: 38px; }
  .nutrition .note { font-size: 9.4px; line-height: 12px; margin-top: 9px; text-align: justify; }

  .contact { position: absolute; top: 574px; left: 0; width: 100%; text-align: center; }
  .contact .web { font-size: 14.5px; font-weight: 400; }
  .contact .mail { font-size: 10.4px; font-weight: 700; line-height: 13px; }

  .sticker {
    position: absolute; top: 630px; width: 192px; height: 87px;
    background: var(--white); border-radius: 14px;
  }
  .sticker--batch { left: 15px; text-align: center; color: var(--sticker-ink);
    font-size: 9.6px; line-height: 11.6px; padding-top: 9px; }
  .sticker--code { left: 232px; }
</style>
</head>
<body>

<section class="sheet sheet--front">
  <div class="label">
    <div class="brand-dot"></div>
    <div class="brand">LEAFMARK</div>
    <div class="tagline">freshest possible</div>
    <div class="front-foot">
      <div class="claim">100% Single Estate Tea</div>
      <div class="divider divider--left"></div>
      <div class="origin-badge" role="img" aria-label="Origin region badge"></div>
      <div class="divider divider--right"></div>
      <div class="weight">Net Wt<br>250g/8.82oz</div>
    </div>
  </div>
</section>

<section class="sheet sheet--rear">
  <div class="label">
    <h1 class="rear-title">TEA LOSES ITS<br>FLAVOUR AND AROMA OVER TIME</h1>

    <div class="copy copy--story">
      <p>Tea tastes good for 24 months after being processed in the factory. Most tea that you get in storespasses through multiple middlemen (like auction house, wholesaler, local exporter etc) and takes between 6-12 months after harvestto reach you. By then tea has already lost a lot of its flavour and aroma.</p>
      <p>We come from a family of small-scaletea growers in Assam, Indiaand will source tea directly from our own tea estates or from similar estates like us. Hence, we are able to tell you when the tea was picked from the garden and when it was packed. By sourcing tea directly from small-scale tea estates, we are removing middlemen, giving a better price to the tea growers and reducing the time it takes to reach tea lovers like yourself.</p>
    </div>

    <div class="nutrition">
      <div class="nutrition-inner">
        <h2>NUTRITIONAL FACTS</h2>
        <div class="nutrition-head"><span>Typical Values</span><span>Per 100ml Brewed Infusion*</span></div>
        <table>
          <tr><td>Energy</td><td>&lt;4 kcal</td></tr>
          <tr><td class="indent">Fat</td><td>0 g</td></tr>
          <tr><td>Of which saturates</td><td>0 g</td></tr>
          <tr><td class="indent">Carbohydrates</td><td>0 g</td></tr>
          <tr><td>Of which sugar</td><td>0 g</td></tr>
          <tr><td>Protein</td><td>&lt;0.5 g</td></tr>
          <tr><td>Salt</td><td>0 g</td></tr>
        </table>
        <p class="note">*Based on an infusion brewed with 200ml water for 3 minutes.</p>
      </div>
    </div>

    <div class="copy copy--guide">
      <h3>WHAT DOES IT TASTE LIKE?</h3>
      <ul><li>Strong, malty, astringent taste and aroma</li></ul>
      <h3>HOW DO I DRINK IT?</h3>
      <ul>
        <li>Rinse the teapot orcup with boiling water</li>
        <li>Add 2 teaspoon (~2 g) of tea leaves into the teapot and then pour boiling water and cover it with the lid</li>
        <li>Allow the tea to brew for one minute. Keep it longer for around three minutes for a stronger brew</li>
        <li>Pour the brew into a cup using a strainer</li>
        <li>Add milk and sugar to taste</li>
      </ul>
    </div>

    <div class="copy copy--facts">
      <h3>INGREDIENTS: BLACK TEA</h3>
      <p>Allergan information: Made in a factory that processes nuts.</p>
      <p style="margin-top:11px"><strong>HOW DO I STORE IT:</strong> Store in an airtight container made of ceramic or tin to keep the light out</p>
      <p class="packer">Packed in the UK<br>by Leafmark Limited,<br>14 Orchard Row, Ashford, TN23 4QP,<br>United Kingdom</p>
    </div>

    <div class="contact">
      <p class="web">Visit our website at www.leafmark.co.uk</p>
      <p class="mail">Write to us at tea@leafmark.co.uk or Leafmark Limited, 14 Orchard Row,<br>Ashford, TN23 4QP, United Kingdom</p>
    </div>

    <div class="sticker sticker--batch">
      “Blank space for sticker”<br>
      Picked on: September 2019<br>
      Packaged on: May 2020<br>
      Best before: May 2022<br>
      Tea type: Black Tea BOP<br>
      Batch no. LOT/12345ABC
    </div>
    <div class="sticker sticker--code"></div>
  </div>
</section>

</body>
</html>
```